Stationery & business cards for nonprofit
WELL Wells of kindness beyond measure
Stationery & business cards for nonprofit - Religion and Spirituality
Creative Brief
Use same font as used in my logo
Ruth Pelling
President
481 Orchard Lane Birmingham, AL 35187
ruth@wellkb.org
www.wellkb.org
We are open to ideas and suggestions using our logo, this is a nonprofit that supports an orphanage and assists widows in Africa, as shown in the earth tone in the logo. Logo information: Font: Desire (manipulated), Swiss Condensed, Times Roman Color: Pantone 1395, Pantone 7407, Pantone 364 Our website is currently under development, but you can see pictures, etc to get a feel for our nonprofit by going to www.wellkb.org
We are thinking to put just the logo on the back of the card with the name (wells of kindness beyond measure) and the verse listed - I John 3:16-18
mirabelcostow mirabelcostow
AI and EPS file formats have been uploaded for use as needed.

```html
<!DOCTYPE html>
<html lang="en">
<head>
<meta charset="utf-8">
<title>WELL – Business Card</title>
<link rel="stylesheet" href="https://fonts.googleapis.com/css2?family=Josefin+Sans:wght@300;400;600&display=swap">
<style>
  :root{
    --bg:#ececec;
    --paper:#ffffff;
    --ink:#3a3a3a;
    --muted:#6b6b6b;
    --gold:#b48a35;
    --green:#4f8a2b;
    --black:#111111;
  }
  *{box-sizing:border-box;margin:0;padding:0}
  html,body{width:1200px;height:906px;overflow:hidden;background:var(--bg);font-family:"Josefin Sans",sans-serif}
  .stage{position:relative;width:1200px;height:906px}
  .card{position:absolute;width:540px;height:309px;box-shadow:0 6px 18px rgba(0,0,0,.12)}
  .card-front{left:50px;top:299px;background:var(--paper)}
  .card-back{left:610px;top:299px;background:var(--black);display:flex;flex-direction:column;align-items:center;justify-content:center}

  .contact-list{position:absolute;list-style:none;display:flex;flex-direction:column;gap:9px}
  .contact-list.primary{left:34px;top:44px}
  .contact-list.secondary{right:34px;bottom:36px}
  .contact-item{display:flex;align-items:center;gap:9px;font-size:11px;color:var(--muted);letter-spacing:.3px}
  .icon{width:15px;height:15px;background:var(--gold);display:flex;align-items:center;justify-content:center;flex:none}
  .icon svg{width:9px;height:9px}

  .identity{position:absolute;left:0;right:0;top:74px;text-align:center}
  .wordmark{display:inline-flex;align-items:center;gap:8px;font-weight:600;font-size:40px;letter-spacing:3px;color:var(--green);line-height:1}
  .wordmark .dot{width:12px;height:12px;border-radius:50%;background:var(--gold)}
  .name{margin-top:18px;font-weight:300;font-size:17px;letter-spacing:1.5px;color:var(--ink);text-transform:uppercase}
  .role{margin-top:4px;font-weight:400;font-size:10px;letter-spacing:2px;color:var(--gold);text-transform:uppercase}

  .card-back .wordmark{color:var(--gold);font-size:56px}
  .tagline{margin-top:10px;font-size:11px;letter-spacing:1.5px;color:var(--gold);text-transform:uppercase}
</style>
</head>
<body>
<main class="stage">
  <section class="card card-front">
    <ul class="contact-list primary">
      <li class="contact-item"><span class="icon"><svg viewBox="0 0 10 10"><path d="M5 0.5a3 3 0 0 0-3 3c0 2.3 3 6 3 6s3-3.7 3-6a3 3 0 0 0-3-3z" fill="#fff"/></svg></span>481 Orchard Lane Birmingham, AL 35187</li>
      <li class="contact-item"><span class="icon"><svg viewBox="0 0 10 10"><path d="M2 1l2 0 1 2.5-1.2 .8a5 5 0 0 0 2 2l.8-1.2L9 6v2a1 1 0 0 1-1 1A7 7 0 0 1 1 2a1 1 0 0 1 1-1z" fill="#fff"/></svg></span>205 555 0148</li>
      <li class="contact-item"><span class="icon"><svg viewBox="0 0 10 10"><rect x="1" y="2" width="8" height="6" fill="#fff"/><path d="M1 2l4 3.2L9 2" stroke="#b48a35" fill="none"/></svg></span>ruth@wellkb.org</li>
    </ul>

    <div class="identity">
      <div class="wordmark"><span class="dot"></span>WELL</div>
      <p class="name">Ruth Pelling</p>
      <p class="role">President</p>
    </div>

    <ul class="contact-list secondary">
      <li class="contact-item"><span class="icon"><svg viewBox="0 0 10 10"><rect x="1" y="2" width="8" height="6" fill="#fff"/><path d="M1 2l4 3.2L9 2" stroke="#b48a35" fill="none"/></svg></span>ruth@wellkb.org</li>
      <li class="contact-item"><span class="icon"><svg viewBox="0 0 10 10"><circle cx="5" cy="5" r="4" fill="none" stroke="#fff"/><path d="M1 5h8M5 1c-2 2.5-2 5.5 0 8M5 1c2 2.5 2 5.5 0 8" stroke="#fff" fill="none" stroke-width=".7"/></svg></span>www.wellkb.org</li>
      <li class="contact-item"><span class="icon"><svg viewBox="0 0 10 10"><circle cx="5" cy="5" r="4" fill="none" stroke="#fff"/><path d="M1 5h8M5 1c-2 2.5-2 5.5 0 8M5 1c2 2.5 2 5.5 0 8" stroke="#fff" fill="none" stroke-width=".7"/></svg></span>wellkb.org/give</li>
    </ul>
  </section>

  <section class="card card-back">
    <div class="wordmark"><span class="dot"></span>WELL</div>
    <p class="tagline">Wells of kindness beyond measure</p>
  </section>
</main>
</body>
</html>
```